Funny (3Romp-alike) Site Design + Code Needed

Hello everybody,

I'm newcomer who want to make a site that could generate income in the future.
I'm interested in funny photo sites like 3romp.
So I need:

- An website that works like 3romp (users post images, comments...)
- The website should have ability to crawl images from 3romp posts then post in my site(every x min/hrs)...
- The web graphic should be design to be clean, fresh, neat as well as there are spots for ads.

In sum, I need an autopilot 3romp-alike site.
I think there are alot of source that looks like 3romp. So the main point here is to design it unique, and make it autopilot.

Any question, please inbox me.
Thanks.

```html
<!DOCTYPE html>
<html lang="en">
<head>
<meta charset="utf-8">
<title>Giggle Hub</title>
<link href="https://fonts.googleapis.com/css2?family=PT+Sans:wght@400;700&family=PT+Sans+Narrow:wght@400;700&display=swap" rel="stylesheet">
<style>
:root{
  --header-top:#3e4a5c;
  --header-bottom:#2a3342;
  --nav-bg:#eef0f3;
  --nav-line:#d7dbe1;
  --nav-text:#4a5260;
  --accent:#2f6fb4;
  --page:#ffffff;
  --panel:#e9ecf0;
  --card-line:#dde0e4;
  --title:#333a44;
  --meta:#8a9099;
  --footer-bg:#f2f3f5;
  --orange:#f26a3a;
}
*{box-sizing:border-box;margin:0;padding:0}
html,body{width:957px;height:1200px;overflow:hidden;background:var(--page);font-family:"PT Sans",sans-serif}
.site-header{height:51px;background:linear-gradient(var(--header-top),var(--header-bottom))}
.header-inner{width:800px;margin:0 auto;height:51px;display:flex;align-items:center;justify-content:space-between}
.site-name{font-family:"PT Sans",sans-serif;font-weight:700;color:#fff;font-size:28px}
.header-actions{display:flex;align-items:center;gap:10px;color:#fff;font-family:"PT Sans Narrow",sans-serif;font-size:13px}
.store-badge{width:22px;height:22px;border-radius:4px;background:#6f8bb0}
.store-badge.alt{background:#5aa36a}
.header-actions .sep{opacity:.5}
.header-actions a{margin-left:10px}
.nav-bar{height:40px;background:var(--nav-bg);border-bottom:1px solid var(--nav-line)}
.nav-inner{width:792px;margin:0 auto;height:40px;display:flex;align-items:stretch}
.nav-item{font-family:"PT Sans Narrow",sans-serif;font-size:14px;color:var(--nav-text);padding:0 15px;display:flex;align-items:center;border-right:1px solid var(--nav-line)}
.nav-item:first-child{border-left:1px solid var(--nav-line);color:var(--accent);background:#e6eaf0}
.nav-item svg{margin-left:6px}
.social-row{display:flex;align-items:center;gap:10px;margin-left:20px}
.social-btn{display:flex;align-items:center;gap:3px;font-size:10px}
.social-btn .btn{border:1px solid #c8cdd4;background:#fff;border-radius:2px;padding:1px 4px;color:#3b4b6b;font-weight:700}
.social-btn .btn.share{background:var(--orange);color:#fff;border-color:var(--orange)}
.social-btn .count{border:1px solid #c8cdd4;background:#fff;padding:1px 4px;color:#555}
.hot-posts{width:792px;height:100px;margin:12px auto 0;background:var(--panel);border-radius:3px;display:flex}
.hot-arrow{width:29px;display:flex;align-items:center;justify-content:center;border-right:1px solid #d6dae0}
.hot-arrow.right{border-right:none;border-left:1px solid #d6dae0}
.hot-body{flex:1;text-align:center}
.hot-title{font-family:"PT Sans Narrow",sans-serif;font-size:17px;color:#3a4656;margin-top:8px}
.thumbs{display:flex;justify-content:center;gap:9px;margin-top:8px}
.thumb{width:63px;height:47px}
.post-grid{width:782px;margin:21px auto 0;display:grid;grid-template-columns:repeat(3,250px);column-gap:16px;row-gap:25px}
.post-card{height:283px;border:1px solid var(--card-line);padding:5px}
.post-image{height:193px;position:relative}
.share-overlay{position:absolute;inset:0;background:rgba(30,34,40,.55);display:flex;flex-direction:column;align-items:center;justify-content:center;gap:10px}
.share-count{color:#fff;font-family:"PT Sans Narrow",sans-serif;font-weight:700;font-size:15px;margin-top:-30px}
.share-icons{display:flex;gap:10px}
.share-dot{width:32px;height:32px;border-radius:50%;border:2px solid #222;display:flex;align-items:center;justify-content:center}
.post-title{font-size:13.5px;line-height:20px;color:var(--title);margin:9px 0 0 6px}
.post-meta{font-size:10.5px;color:var(--meta);margin:8px 0 0 5px;white-space:nowrap;font-family:"PT Sans Narrow",sans-serif}
.post-meta b{font-weight:400;color:#555}
.post-meta .sep{margin:0 8px}
.site-footer{position:absolute;top:1148px;left:0;width:957px;height:52px;background:var(--footer-bg);border-top:1px solid #e3e5e8}
.footer-inner{width:800px;margin:0 auto;height:52px;display:flex;align-items:center;justify-content:space-between;font-size:10.5px;color:#6c727b}
.to-top{display:flex;align-items:center;gap:8px;font-size:9px;color:#8a9099}
.to-top span.circle{width:29px;height:29px;border-radius:50%;background:#c3c7cd;display:flex;align-items:center;justify-content:center}
</style>
</head>
<body>
<header class="site-header">
  <div class="header-inner">
    <div class="site-name">GIGGLE HUB</div>
    <div class="header-actions">
      <span class="store-badge"></span>
      <span class="store-badge alt"></span>
      <a>LOG IN</a><span class="sep">|</span><a style="margin-left:0">REGISTER</a>
    </div>
  </div>
</header>
<nav class="nav-bar">
  <div class="nav-inner">
    <div class="nav-item">LATEST</div>
    <div class="nav-item">POPULAR</div>
    <div class="nav-item">TRENDING</div>
    <div class="nav-item">MORE<svg width="8" height="5"><path d="M0 0l4 4 4-4" stroke="#4a5260" fill="none"/></svg></div>
    <div class="nav-item" style="padding:0 20px">PROFILE SETTINGS<svg width="8" height="5"><path d="M0 0l4 4 4-4" stroke="#4a5260" fill="none"/></svg></div>
    <div class="social-row">
      <div class="social-btn"><span class="btn">Like</span><span class="count">3k</span></div>
      <div class="social-btn"><span class="btn">Post</span><span class="count">316</span></div>
      <div class="social-btn"><span class="btn">+1</span><span class="count">81</span></div>
      <div class="social-btn"><span class="btn share">Share</span><span class="count">4.6K</span></div>
    </div>
  </div>
</nav>
<section class="hot-posts">
  <div class="hot-arrow"><svg width="9" height="16"><path d="M9 0L0 8l9 8z" fill="#9aa3ae"/></svg></div>
  <div class="hot-body">
    <div class="hot-title">HOT POSTS</div>
    <div class="thumbs">
      <div class="thumb" role="img" aria-label="Hot post thumbnail" style="background:#8a8f6e"></div>
      <div class="thumb" role="img" aria-label="Hot post thumbnail" style="background:#c9b9a6"></div>
      <div class="thumb" role="img" aria-label="Hot post thumbnail" style="background:#5b6a72"></div>
      <div class="thumb" role="img" aria-label="Hot post thumbnail" style="background:#a68c74"></div>
      <div class="thumb" role="img" aria-label="Hot post thumbnail" style="background:#4a3a4a"></div>
      <div class="thumb" role="img" aria-label="Hot post thumbnail" style="background:#7aa0c4"></div>
      <div class="thumb" role="img" aria-label="Hot post thumbnail" style="background:#b08a78"></div>
      <div class="thumb" role="img" aria-label="Hot post thumbnail" style="background:#5e5a4e"></div>
      <div class="thumb" role="img" aria-label="Hot post thumbnail" style="background:#c4493a"></div>
      <div class="thumb" role="img" aria-label="Hot post thumbnail" style="background:#6f6a63"></div>
    </div>
  </div>
  <div class="hot-arrow right"><svg width="9" height="16"><path d="M0 0l9 8-9 8z" fill="#9aa3ae"/></svg></div>
</section>
<main class="post-grid">
  <article class="post-card"><div class="post-image" role="img" aria-label="Photo of an elderly woman making a rock hand sign" style="background:linear-gradient(#a08a6e,#6e5238)"></div><p class="post-title">Pellentesque tortor lectus, auctor porta fringilla et, consequat nec</p><p class="post-meta">October 30, 2013<span class="sep">|</span>( <b>53</b> ) Like<span class="sep">|</span>( <b>21</b> ) Comment</p></article>
  <article class="post-card"><div class="post-image" role="img" aria-label="Photo of a dog in a costume on a street" style="background:linear-gradient(#5a6068,#3e4248)"><div class="share-overlay"><div class="share-count">230 SHARES</div><div class="share-icons"><span class="share-dot" style="background:#3b5fb0"></span><span class="share-dot" style="background:#3fb8e8"></span><span class="share-dot" style="background:#e8674e"></span><span class="share-dot" style="background:#f05a3a"></span><span class="share-dot" style="background:#fff"><svg width="14" height="14"><circle cx="11" cy="3" r="2" fill="#222"/><circle cx="3" cy="7" r="2" fill="#222"/><circle cx="11" cy="11" r="2" fill="#222"/><path d="M11 3L3 7l8 4" stroke="#222" fill="none" stroke-width="1.5"/></svg></span></div></div></div><p class="post-title">Pellentesque tortor lectus, auctor porta fringilla et, consequat nec</p><p class="post-meta">October 30, 2013<span class="sep">|</span>( <b>53</b> ) Like<span class="sep">|</span>( <b>21</b> ) Comment</p></article>
  <article class="post-card"><div class="post-image" role="img" aria-label="Photo of a man beside a hippo in a river" style="background:linear-gradient(#c9d0c8,#7c8a70 45%,#5a5a48)"></div><p class="post-title">Pellentesque tortor lectus, auctor porta fringilla et, consequat nec</p><p class="post-meta">October 30, 2013<span class="sep">|</span>( <b>53</b> ) Like<span class="sep">|</span>( <b>21</b> ) Comment</p></article>
  <article class="post-card"><div class="post-image" role="img" aria-label="Photo of a child on a skateboard by a steep road to the sea" style="background:linear-gradient(#3a6a78,#8a8e70 55%,#6a6c58)"></div><p class="post-title">Pellentesque tortor lectus, auctor porta fringilla et, consequat nec</p><p class="post-meta">October 30, 2013<span class="sep">|</span>( <b>53</b> ) Like<span class="sep">|</span>( <b>21</b> ) Comment</p></article>
  <article class="post-card"><div class="post-image" role="img" aria-label="Photo of a person riding a chalk-drawn bicycle" style="background:linear-gradient(#9a9aa0,#7a7a82)"></div><p class="post-title">Pellentesque tortor lectus, auctor porta fringilla et, consequat nec</p><p class="post-meta">October 30, 2013<span class="sep">|</span>( <b>53</b> ) Like<span class="sep">|</span>( <b>21</b> ) Comment</p></article>
  <article class="post-card"><div class="post-image" role="img" aria-label="Photo of a grinning dog" style="background:linear-gradient(#b8ab90,#8a7c66)"></div><p class="post-title">Pellentesque tortor lectus, auctor porta fringilla et, consequat nec</p><p class="post-meta">October 30, 2013<span class="sep">|</span>( <b>53</b> ) Like<span class="sep">|</span>( <b>21</b> ) Comment</p></article>
  <article class="post-card"><div class="post-image" role="img" aria-label="Photo of a white cat biting a cactus" style="background:linear-gradient(#3a3a38,#8a9a78)"></div><p class="post-title">Pellentesque tortor lectus, auctor porta fringilla et, consequat nec</p><p class="post-meta">October 30, 2013<span class="sep">|</span>( <b>53</b> ) Like<span class="sep">|</span>( <b>21</b> ) Comment</p></article>
  <article class="post-card"><div class="post-image" role="img" aria-label="Photo of cup art in a fence" style="background:linear-gradient(#4a78b8,#b05040 50%,#8a8a88)"></div><p class="post-title">Pellentesque tortor lectus, auctor porta fringilla et, consequat nec</p><p class="post-meta">October 30, 2013<span class="sep">|</span>( <b>53</b> ) Like<span class="sep">|</span>( <b>21</b> ) Comment</p></article>
  <article class="post-card"><div class="post-image" role="img" aria-label="Photo of a cat with glasses reading a newspaper" style="background:linear-gradient(#8a5a30,#c29a6a)"></div><p class="post-title">Pellentesque tortor lectus, auctor porta fringilla et, consequat nec</p><p class="post-meta">October 30, 2013<span class="sep">|</span>( <b>53</b> ) Like<span class="sep">|</span>( <b>21</b> ) Comment</p></article>
</main>
<footer class="site-footer">
  <div class="footer-inner">
    <span>Copyright © 2013 Giggle Hub. All rights reserved.</span>
    <span class="to-top">Top<span class="circle"><svg width="14" height="12"><path d="M7 0L14 8H10V12H4V8H0z" fill="#fff"/></svg></span></span>
  </div>
</footer>
</body>
</html>
```